Brochure design for trade company

I would like to get a professional, easy to read and eye catchy capability statement designed for my electrical business.

My aim is to be able to go to property managers and WOW them when they see the capability statement.

Attached the content writing, design brief, company logo and template of what I like below. If there are any questions please send me a message.

The areas we service photo is an example, please do your own designs for the maps section

Thank you in advance for the help team.

Requirements
Must have
• The areas we service photo is an example, please do your own designs for the maps section
Nice to have
• Eye catching and creative. Also be warm & inviting
Should not have
• Not too out of place looking photos or elements. Don’t make it he design look too cold

```html
<!DOCTYPE html>
<html lang="en">
<head>
<meta charset="utf-8">
<title>Voltline Electrical – Capability Statement</title>
<link href="https://fonts.googleapis.com/css2?family=Oswald:wght@500;700&family=Open+Sans:wght@400;600;700&display=swap" rel="stylesheet">
<style>
:root{
  --bg:#ebebeb;
  --paper:#ffffff;
  --yellow:#f6b81c;
  --ink:#262626;
  --grey:#6b6b6b;
  --navy:#1d2438;
  --night1:#1a2a4a;
  --night2:#3c5a86;
}
*{box-sizing:border-box;margin:0;padding:0}
html,body{width:849px;height:1200px;overflow:hidden;background:var(--bg)}
body{position:relative;font-family:"Open Sans",Arial,sans-serif;color:var(--ink)}
.page{position:absolute;width:289px;height:395px;background:var(--paper);overflow:hidden;box-shadow:0 1px 4px rgba(0,0,0,.12)}
.page--cover{left:62px;top:113px}
.page--photo{left:498px;top:113px}
.page--about{left:62px;top:645px}
.page--service{left:498px;top:645px}
.head{font-family:"Oswald",Arial,sans-serif;font-weight:700;text-transform:uppercase;line-height:1.05}
.tag-block{position:absolute;left:0;top:0;z-index:2;background:var(--yellow);padding:14px 6px;width:92px;display:flex;align-items:center;justify-content:center}
.tag-block .head{font-size:14px;text-align:center;color:var(--ink)}
.brand{position:absolute;display:flex;align-items:center;gap:4px;font-family:"Oswald",Arial,sans-serif;font-weight:700;font-size:12px;color:var(--ink);letter-spacing:.5px}
.brand-dot{width:7px;height:7px;background:var(--yellow);border-radius:50%}
.photo{position:absolute}
.cover-title{position:absolute;z-index:2;left:112px;top:102px;width:177px;background:var(--navy);padding:6px 8px 7px}
.small{font-size:4.6px;line-height:1.45;color:var(--grey)}
.h-sub{font-family:"Oswald",Arial,sans-serif;font-weight:700;font-size:7.5px;text-transform:uppercase;color:var(--ink);margin-bottom:4px}
ul.list{list-style:none}
ul.list li{font-size:4.6px;line-height:1.6;color:var(--grey);padding-left:6px;position:relative}
ul.list li::before{content:"";position:absolute;left:0;top:2.6px;width:3px;height:3px;background:var(--yellow)}
</style>
</head>
<body>

<section class="page page--cover">
  <div class="tag-block" style="height:86px">
    <p class="head">When<br>Quality<br>and<br>Reliability<br>Counts</p>
  </div>
  <div class="brand" style="right:14px;top:16px"><span class="brand-dot"></span>VOLTLINE</div>
  <div style="position:absolute;z-index:2;left:112px;top:88px;background:var(--yellow);padding:2px 6px;font-family:'Oswald',sans-serif;font-weight:500;font-size:7px;text-transform:uppercase;color:var(--ink)">Service Division</div>
  <div class="cover-title">
    <p class="head" style="color:#fff;font-size:17px">Capability<br>Statement</p>
  </div>
  <div class="photo" role="img" aria-label="City skyline at night reflected in a river" style="left:0;top:140px;width:289px;height:200px;background:linear-gradient(180deg,var(--night1) 0%,var(--night2) 55%,#caa25a 72%,#1a2540 100%)"></div>
  <div style="position:absolute;left:0;top:352px;width:289px;text-align:center;font-family:'Oswald',sans-serif;font-size:6.5px;color:var(--ink);text-transform:uppercase">Residential | Commercial | Real Estate | Strata</div>
  <div style="position:absolute;left:0;top:366px;width:289px;height:14px;background:var(--yellow);text-align:right;padding-right:12px;font-size:5px;line-height:14px;font-weight:600">www.voltline.example</div>
</section>

<section class="page page--photo">
  <div class="photo" role="img" aria-label="Yellow hard hat, work gloves and coloured electrical wires" style="left:0;top:0;width:289px;height:395px;background:linear-gradient(160deg,#f7c93a 0%,#f3d98a 30%,#e9e3d6 55%,#d98a4a 75%,#5f8fb8 100%)"></div>
  <p class="small" style="position:absolute;left:14px;bottom:14px;color:#444">Licensed electricians serving your properties.</p>
</section>

<section class="page page--about">
  <div class="tag-block" style="width:110px;height:92px">
    <p class="head" style="font-size:15px">About<br>Voltline<br>Electrical</p>
  </div>
  <div class="photo" role="img" aria-label="Glowing light bulb against a dark background" style="left:110px;top:0;width:179px;height:92px;background:radial-gradient(circle at 45% 55%,#f2c15a 0%,#7a5220 22%,#1c1c1c 55%)"></div>
  <div style="position:absolute;left:14px;top:104px;width:122px">
    <p class="h-sub">Who We Are</p>
    <p class="small">Voltline Electrical is a locally owned team of licensed electricians supporting property managers, owners and strata groups. We deliver safe, compliant and tidy work on time, with clear quotes and friendly service from first call to final sign off.</p>
    <p class="small" style="margin-top:4px">Our crew holds full licences and insurance for every job we complete.</p>
    <p class="h-sub" style="margin-top:12px">Core Values</p>
    <ul class="list">
      <li>Safety on every site</li>
      <li>Honest, upfront pricing</li>
      <li>Reliable, on-time service</li>
      <li>Respect for your tenants</li>
    </ul>
  </div>
  <div style="position:absolute;left:152px;top:104px;width:124px">
    <p class="h-sub">Our Promise To You</p>
    <ul class="list">
      <li>Prompt response to all maintenance requests</li>
      <li>Clear written quotes before any work starts</li>
      <li>Photo reports sent after each job is done</li>
      <li>Clean, safe work areas left behind</li>
      <li>Direct contact with your own electrician</li>
    </ul>
    <p class="h-sub" style="margin-top:12px">Areas We Service</p>
    <div role="img" aria-label="Map of the service area" style="width:124px;height:92px;background:linear-gradient(135deg,#e2e2e2,#cfcfcf)"></div>
  </div>
  <div style="position:absolute;left:0;bottom:0;width:289px;height:10px;background:var(--yellow)"></div>
</section>

<section class="page page--service">
  <div class="photo" role="img" aria-label="Switchboard with circuit breakers" style="left:0;top:0;width:289px;height:120px;background:linear-gradient(120deg,#3a3a3a 0%,#8d8d8d 45%,#d8d8d8 70%,#6a6a6a 100%)"></div>
  <div class="tag-block" style="width:100px;height:120px">
    <p class="head" style="font-size:13px">Service<br>&amp;<br>Maintenance</p>
  </div>
  <div style="position:absolute;left:14px;top:132px;width:260px">
    <p class="h-sub">Our Maintenance Services</p>
    <ul class="list">
      <li>Lighting repairs and LED upgrades</li>
      <li>Power point and switch replacement</li>
      <li>Switchboard upgrades and safety switches</li>
      <li>Smoke alarm testing and compliance</li>
      <li>Fault finding and emergency call outs</li>
      <li>Ceiling fans and exhaust fans</li>
      <li>Data, TV and phone points</li>
      <li>Common area and strata lighting</li>
      <li>End of lease electrical inspections</li>
      <li>Pre-purchase and rental safety checks</li>
    </ul>
  </div>
  <div style="position:absolute;left:0;top:300px;width:289px;height:95px;background:var(--yellow);padding:12px 14px">
    <p class="head" style="font-size:12px;color:var(--ink)">Contact and Licences</p>
    <p style="font-size:5px;line-height:1.6;margin-top:6px;font-weight:600">Voltline Electrical Pty Ltd</p>
    <p style="font-size:5px;line-height:1.6">Phone: 0400 123 456</p>
    <p style="font-size:5px;line-height:1.6">Email: hello@voltline.example</p>
    <p style="font-size:5px;line-height:1.6">Electrical Licence No. 000000</p>
    <p style="font-size:5px;line-height:1.6">www.voltline.example</p>
  </div>
</section>

</body>
</html>
```